Website for Apartment Rental in Prague

I would like to create designs of my website focused on luxury apartment rentals in Prague, Czech Republic. I created initial mock-ups, They are all attached. I need to design homepage and subpage. The mock-ups were created by combining elements from different websites that I liked but I need you to create a design that is unique and original. The attached files a only a guidance for the structure of the website but not for the design. Try to be creative.

Industry/Entity Type

Apartment

```html
<!DOCTYPE html>
<html lang="en">
<head>
<meta charset="utf-8">
<title>Vltava Residences – Luxury Apartments in Prague</title>
<link href="https://fonts.googleapis.com/css2?family=Open+Sans:wght@300;400;600;700&display=swap" rel="stylesheet">
<style>
:root{
  --gold:#8b7752;
  --gold-dark:#74633f;
  --gold-light:#b09a6e;
  --ink:#222;
  --text:#555;
  --muted:#888;
  --line:#e4e4e4;
  --soft:#f4f4f4;
  --dark:#2b2d33;
}
*{box-sizing:border-box;margin:0;padding:0}
html,body{width:1200px;height:3303px;overflow:hidden}
body{font-family:"Open Sans",Arial,sans-serif;color:var(--text);background:#fff;position:relative}
.abs{position:absolute}
a{color:inherit;text-decoration:none}

/* top bar */
.topbar{position:absolute;left:0;top:0;width:1200px;height:44px;background:var(--gold);color:#fff;font-size:13px;display:flex;align-items:center;padding:0 80px;justify-content:space-between}
.topbar .contact{display:flex;align-items:center;gap:14px}
.topbar .ic{width:30px;height:30px;border:1px solid rgba(255,255,255,.7);border-radius:50%;display:inline-flex;align-items:center;justify-content:center}
.topbar .links{display:flex;gap:14px;align-items:center}

/* header */
.header{position:absolute;top:44px;left:0;width:1200px;height:101px;display:flex;align-items:center;justify-content:space-between;padding:0 80px}
.brand{font-weight:700;font-size:26px;letter-spacing:4px;color:var(--ink)}
.nav{display:flex;gap:37px;font-size:15px;color:#444}

/* hero */
.hero{position:absolute;top:145px;left:0;width:1200px;height:531px;background:linear-gradient(120deg,#3b2618 0%,#6b4528 35%,#4a3020 60%,#2a2220 100%)}
.hero h1{position:absolute;left:78px;top:300px;font-size:46px;font-weight:400;color:#fff;line-height:1.2;letter-spacing:.5px}
.hero-btns{position:absolute;left:78px;top:436px;display:flex;gap:20px}
.btn-white{background:#fff;color:#222;font-size:15px;font-weight:600;height:50px;padding:0 26px;display:flex;align-items:center;border-radius:3px}
.booking{position:absolute;left:799px;top:180px;width:335px;height:496px;background:#fff;border-radius:4px 4px 0 0;padding:34px 22px 0;text-align:center}
.booking h2{font-weight:400;font-size:30px;color:var(--ink)}
.booking .sub{font-size:15px;color:var(--muted);margin:6px 0 24px}
.field{height:50px;border:1px solid #ddd;border-radius:3px;font-size:12px;color:#aaa;display:flex;align-items:center;padding:0 10px;margin-bottom:8px;text-align:left}
.row{display:flex;gap:6px}
.row .field{flex:1;justify-content:space-between}
.caret{width:8px;height:8px;border-right:2px solid #666;border-bottom:2px solid #666;transform:rotate(45deg);margin-top:-4px}
.check{margin-top:12px;height:50px;border-radius:4px;background:linear-gradient(#b5a077,var(--gold-dark));color:#fff;font-weight:700;font-size:20px;display:flex;align-items:center;justify-content:center}

/* vision */
.vision{position:absolute;top:676px;left:0;width:1200px;height:344px;overflow:hidden}
.vision .txt{position:absolute;top:100px;left:0;width:1200px;text-align:center}
h2.title{font-size:37px;font-weight:400;color:var(--ink);letter-spacing:.5px;text-align:center}
.lead{font-size:13px;line-height:24px;color:#555;margin-top:14px}

/* features */
.features{position:absolute;top:1020px;left:0;width:1200px;height:407px;background:linear-gradient(100deg,#22252c 0%,#3a3d45 45%,#595449 75%,#7a705c 100%)}
.feat{position:absolute;width:300px;text-align:center;color:#fff}
.feat .circ{width:124px;height:124px;border-radius:50%;background:#fff;margin:0 auto;display:flex;align-items:center;justify-content:center}
.feat h3{font-size:22px;font-weight:400;margin-top:20px}
.feat p{font-size:14px;line-height:22px;color:#ddd;margin-top:8px}

/* featured */
.featured{position:absolute;top:1427px;left:0;width:1200px;height:632px;background:#f2f2f2;overflow:hidden}
.card{position:absolute;top:167px;width:336px;height:405px;background:#fff;box-shadow:0 1px 4px rgba(0,0,0,.1)}
.card .ph{position:absolute;left:11px;top:11px;width:314px;height:210px}
.price{position:absolute;right:11px;top:174px;background:var(--gold);color:#fff;font-size:19px;padding:0 14px;height:47px;display:flex;align-items:center}
.card h4{position:absolute;left:24px;top:236px;right:24px;font-size:18px;font-weight:400;color:var(--ink);line-height:24px}
.card .addr{position:absolute;left:24px;top:296px;right:24px;font-size:14px;color:#666;line-height:22px}
.card .meta{position:absolute;left:0;right:0;top:355px;border-top:1px solid var(--line);height:50px;display:flex;align-items:center;gap:30px;padding-left:22px;font-size:13px;color:#777}
.meta span{display:flex;gap:6px;align-items:center}

/* interiors */
.interiors{position:absolute;top:2059px;left:0;width:1200px;height:286px;overflow:hidden}
.interiors .txt{position:absolute;top:76px;left:110px;width:980px;text-align:center}

/* news */
.news{position:absolute;top:2345px;left:0;width:1200px;height:478px;background:var(--soft)}
.news-card{position:absolute;top:139px;width:418px}
.news-card .ph{height:165px;border:1px solid #333}
.news-card .hd{display:flex;justify-content:space-between;align-items:baseline;margin-top:20px}
.news-card h5{font-size:19px;font-weight:400;color:var(--ink)}
.news-card .date{font-size:13px;color:#555}
.news-card p{font-size:13px;line-height:21px;color:#666;margin-top:10px}

/* newsletter */
.newsletter{position:absolute;top:2823px;left:0;width:1200px;height:165px;background:var(--gold);overflow:hidden}
.newsletter h3{position:absolute;left:80px;top:36px;font-size:37px;font-weight:400;color:#fff;line-height:42px}
.mailring{position:absolute;left:405px;top:-8px;width:130px;height:130px;border:1px solid rgba(255,255,255,.7);border-radius:50%;display:flex;align-items:center;justify-content:center;margin-top:28px}
.email{position:absolute;left:508px;top:56px;width:417px;height:52px;background:#fff;border-radius:4px;font-size:13px;font-style:italic;color:#999;display:flex;align-items:center;padding-left:20px}
.subscribe{position:absolute;left:936px;top:56px;width:187px;height:52px;background:#fff;border-radius:4px;color:var(--gold-dark);font-size:18px;letter-spacing:1px;display:flex;align-items:center;justify-content:center}

/* footer */
.footer{position:absolute;top:2988px;left:0;width:1200px;height:231px;display:flex}
.fcol{padding:30px 0 0 0;position:relative}
.fcol h6{font-size:20px;font-weight:400;color:var(--ink);border-left:4px solid var(--gold);padding-left:14px;line-height:22px}
.fcol.sep{border-left:1px solid var(--line)}
.flinks{display:grid;grid-template-columns:135px 200px;row-gap:14px;margin:26px 0 0 18px;font-size:13px;color:#777}
.flinks .on{color:#222}
.fcontact{margin:24px 0 0 18px;font-size:14px;color:#777}
.fcontact div{display:flex;gap:16px;margin-bottom:16px;line-height:22px}
.fabout{margin:24px 30px 0 22px;font-size:14px;line-height:22px;color:#888}
.copy{position:absolute;top:3219px;left:0;width:1200px;height:84px;background:var(--gold);color:#fff;font-size:14px;display:flex;align-items:center;justify-content:center}
</style>
</head>
<body>

<div class="topbar">
  <div class="contact">
    <span>CONTACT US NOW :</span>
    <span class="ic"><svg width="14" height="14" viewBox="0 0 24 24"><path fill="#fff" d="M6.6 10.8a15 15 0 0 0 6.6 6.6l2.2-2.2c.3-.3.7-.4 1-.2 1.1.4 2.3.6 3.6.6.6 0 1 .4 1 1V20c0 .6-.4 1-1 1A17 17 0 0 1 3 4c0-.6.4-1 1-1h3.5c.6 0 1 .4 1 1 0 1.3.2 2.5.6 3.6.1.3 0 .7-.2 1z"/></svg></span>
    <span>+420 555 010 200</span>
    <span class="ic"><svg width="14" height="12" viewBox="0 0 24 18"><rect x="1" y="1" width="22" height="16" rx="2" fill="none" stroke="#fff" stroke-width="2"/><path d="M1 2l11 8 11-8" fill="none" stroke="#fff" stroke-width="2"/></svg></span>
    <span>hello@vltavaresidences.com</span>
  </div>
  <div class="links"><span>DISCOVER PRAGUE</span><span>|</span><span>OUR HOSPITALITY</span><span>|</span><span>EN ▾</span></div>
</div>

<header class="header">
  <div class="brand">VLTAVA RESIDENCES</div>
  <nav class="nav"><a>Apartment</a><a>Services</a><a>Gallery</a><a>News</a><a>Exclusive offer &amp; Tours</a><a>For Families</a><a>Contact</a></nav>
</header>

<section class="hero" role="img" aria-label="Photo of a warm wood-panelled luxury living room with sofas">
  <h1>WE'LL HELP YOU FIND YOUR<br>NEW HOME</h1>
  <div class="hero-btns"><a class="btn-white">FIND OUT MORE</a><a class="btn-white">BOOK AN APPOINTMENT</a></div>
</section>

<form class="booking">
  <h2>OFFICIAL SITE</h2>
  <div class="sub">Best Price Guaranteed</div>
  <div class="field">Full Name</div>
  <div class="row"><div class="field">Adults <i class="caret"></i></div><div class="field">Child <i class="caret"></i></div><div class="field">Infant <i class="caret"></i></div></div>
  <div class="row"><div class="field">Check In <i class="caret"></i></div><div class="field">Check Out <i class="caret"></i></div></div>
  <div class="field">Promotional Code</div>
  <div class="field">Select Rental Unit</div>
  <div class="check">Check Availability</div>
</form>

<section class="vision">
  <svg class="abs" style="left:0;top:0" width="1200" height="344">
    <polygon points="700,0 1200,0 1200,344 1020,344" fill="#ececf0"/>
    <polygon points="0,60 280,344 0,344" fill="#f2a83a"/>
  </svg>
  <div class="abs" role="img" aria-label="Photo of a sunset seen through a window" style="left:0;top:60px;width:280px;height:284px;clip-path:polygon(0 0,100% 100%,0 100%);background:linear-gradient(160deg,#7a4a1c,#f5b23a 55%,#ffd97a)"></div>
  <div class="txt">
    <h2 class="title">A DIFFERENT VISION OF TRAVELLING</h2>
    <p class="lead">Something spectacular has arrived in the heart of Europe.<br>Steps from Old Town, this rental experience is curated with world-class amenities, exemplary style and a level of convenience you have to experience to believe.<br>Experience the different vision of luxury in the center of Prague.</p>
  </div>
  <svg class="abs" style="left:578px;top:324px" width="44" height="20"><polygon points="0,20 22,0 44,20" fill="#2b2d33"/></svg>
</section>

<section class="features" role="img" aria-label="Dim photo of a modern apartment interior behind the feature icons">
  <svg class="abs" style="left:0;top:0" width="44" height="1"></svg>
  <svg class="abs" style="left:578px;top:0" width="44" height="22"><polygon points="0,0 44,0 22,22" fill="#fff"/><path d="M16 4l6 6 6-6M16 10l6 6 6-6" stroke="#333" stroke-width="2" fill="none"/></svg>
  <svg class="abs" style="left:360px;top:100px" width="540" height="80"><path d="M0 30 Q80 0 160 50" stroke="#fff" stroke-dasharray="5 5" fill="none"/><path d="M152 40l8 10-12 2" stroke="#fff" fill="none"/><path d="M320 50 Q400 0 470 30" stroke="#fff" stroke-dasharray="5 5" fill="none"/><path d="M460 22l10 8-12 4" stroke="#fff" fill="none"/></svg>
  <div class="feat" style="left:123px;top:85px">
    <div class="circ"><svg width="56" height="60" viewBox="0 0 56 60"><rect x="8" y="6" width="40" height="52" fill="none" stroke="#8b7752" stroke-width="3"/><g fill="#8b7752"><rect x="15" y="14" width="8" height="7"/><rect x="33" y="14" width="8" height="7"/><rect x="15" y="27" width="8" height="7"/><rect x="33" y="27" width="8" height="7"/><rect x="24" y="44" width="8" height="14"/></g></svg></div>
    <h3>APARTMENTS</h3>
    <p>also available to rent all the apartment<br>together for companies or larger groups.</p>
  </div>
  <div class="feat" style="left:445px;top:105px">
    <div class="circ"><svg width="60" height="60" viewBox="0 0 60 60"><circle cx="30" cy="30" r="22" fill="none" stroke="#8b7752" stroke-width="3"/><path d="M30 16v15l10 6" stroke="#8b7752" stroke-width="3" fill="none"/></svg></div>
    <h3>CHECK-OUT</h3>
    <p>12 noon; earliest check-in,<br>3pm- both are flexible,<br>by arrangement.</p>
  </div>
  <div class="feat" style="left:770px;top:85px">
    <div class="circ"><svg width="56" height="56" viewBox="0 0 56 56"><rect x="6" y="12" width="44" height="34" rx="4" fill="none" stroke="#8b7752" stroke-width="3"/><rect x="34" y="24" width="16" height="10" fill="#8b7752"/></svg></div>
    <h3>RATES</h3>
    <p>price from 150 USD per night,<br>including tax.</p>
  </div>
</section>

<section class="featured">
  <svg class="abs" style="left:0;top:0" width="1200" height="632"><polygon points="700,0 1200,0 1200,220" fill="#e4e4ea"/></svg>
  <h2 class="title abs" style="left:0;top:45px;width:1200px">FEATURED PROPERTY</h2>
  <p class="abs" style="left:0;top:112px;width:1200px;text-align:center;font-size:13px;color:#555">Something spectacular has arrived in the heart of Europe.Steps from Old Town, this rental experience.</p>

  <article class="card" style="left:77px">
    <div class="ph" role="img" aria-label="Photo of a penthouse living room with city view" style="background:linear-gradient(135deg,#cfd6da,#8a8070 60%,#3f3a33)"></div>
    <div class="price">From $30,000</div>
    <h4>Brand New Modern Apartment Location</h4>
    <p class="addr">123 Building Name, Street Name, Area, City, Country - Zipcode</p>
    <div class="meta"><span>▬ 3 Beds</span><span>● 1 Bath</span></div>
  </article>
  <article class="card" style="left:433px">
    <div class="ph" role="img" aria-label="Photo of a bright white living room with striped rug" style="background:linear-gradient(135deg,#f2f2f0,#d8d6d2 60%,#9a8c78)"></div>
    <div class="price">From $30,000</div>
    <h4>Brand New Modern Apartment Location</h4>
    <p class="addr">123 Building Name, Street Name, Area, City, Country - Zipcode</p>
    <div class="meta"><span>▬ 3 Beds</span><span>● 1 Bath</span></div>
  </article>
  <article class="card" style="left:788px">
    <div class="ph" role="img" aria-label="Photo of a modern lounge with dark stone fireplace wall" style="background:linear-gradient(135deg,#e6e2dc,#8e8478 55%,#4a4440)"></div>
    <div class="price">From $30,000</div>
    <h4>Brand New Modern Apartment Location</h4>
    <p class="addr">123 Building Name, Street Name, Area, City, Country - Zipcode</p>
    <div class="meta"><span>▬ 3 Beds</span><span>● 1 Bath</span></div>
  </article>
</section>

<section class="interiors">
  <svg class="abs" style="left:0;top:0" width="1200" height="286"><polygon points="0,0 290,0 0,290" fill="#fbeee4"/></svg>
  <svg class="abs" style="left:585px;top:0" width="30" height="24"><path d="M8 4l7 7 7-7M8 11l7 7 7-7" stroke="#333" stroke-width="2" fill="none"/></svg>
  <div class="txt">
    <h2 class="title">INTERIORS DESIGNED BY MAISON LUMEN</h2>
    <p class="lead">Maison Lumen apartments offers short term and as well as long term options in our studio apartments and our one bedroom apartment homes. Our luxurious apartments and high quality customer services have allowed us to dominate the prague apartment market with a proven track record. Our years of experience and knowledge have made us a premier apartment rental company as we continue to stress the importance of servicing individuals and corporations who are seeking the finest accommodations.</p>
  </div>
</section>

<section class="news">
  <h2 class="title abs" style="left:0;top:54px;width:1200px">LATEST NEWS</h2>
  <article class="news-card" style="left:176px">
    <div class="ph" role="img" aria-label="Photo of a white seaside lounge with ocean view" style="background:linear-gradient(180deg,#cfe3ee,#8fb5c9 45%,#e9e6e0 60%,#c9c2b6)"></div>
    <div class="hd"><h5>News Title</h5><span class="date">Date : 15 Oct 2017</span></div>
    <p>Lorem Ipsum is simply dummy text of the printing and typesetting industry.</p>
  </article>
  <article class="news-card" style="left:634px">
    <div class="ph" role="img" aria-label="Photo of a bright living room with bookshelf and striped rug" style="background:linear-gradient(135deg,#f3f3f1,#d6d3cd 60%,#9d8f79)"></div>
    <div class="hd"><h5>News Title</h5><span class="date">Date : 15 Oct 2017</span></div>
    <p>Lorem Ipsum is simply dummy text of the printing and typesetting industry.</p>
  </article>
</section>

<section class="newsletter">
  <h3>SIGNUP FOR<br>NEWSLETTER</h3>
  <div class="mailring" style="top:0"><svg width="46" height="32" viewBox="0 0 46 32"><rect x="1" y="1" width="44" height="30" fill="none" stroke="#fff" stroke-width="2"/><path d="M1 1l22 17L45 1M1 31l16-14M45 31L29 17" fill="none" stroke="#fff" stroke-width="2"/></svg></div>
  <div class="email">Enter Your Email Address</div>
  <div class="subscribe">SUBSCRIBE</div>
</section>

<footer class="footer">
  <div class="fcol" style="width:373px;padding-left:78px">
    <h6>USEFUL LINKS</h6>
    <div class="flinks"><span class="on">Home</span><span>News</span><span>Apartment</span><span>Exclusive offer &amp; Tours</span><span>Services</span><span>For Families</span><span>Gallery</span><span>Contact Us</span></div>
  </div>
  <div class="fcol sep" style="width:410px;padding-left:18px">
    <h6>CONTACT US</h6>
    <div class="fcontact">
      <div><svg width="18" height="22" viewBox="0 0 18 22"><path d="M9 0a8 8 0 0 0-8 8c0 6 8 14 8 14s8-8 8-14a8 8 0 0 0-8-8z" fill="#8b7752"/><circle cx="9" cy="8" r="3" fill="#fff"/></svg><span>123,Lorem ipsum dummy text,<br>Country-123456.</span></div>
      <div><svg width="18" height="18" viewBox="0 0 24 24"><path fill="#8b7752" d="M6.6 10.8a15 15 0 0 0 6.6 6.6l2.2-2.2c.3-.3.7-.4 1-.2 1.1.4 2.3.6 3.6.6.6 0 1 .4 1 1V20c0 .6-.4 1-1 1A17 17 0 0 1 3 4c0-.6.4-1 1-1h3.5c.6 0 1 .4 1 1 0 1.3.2 2.5.6 3.6.1.3 0 .7-.2 1z"/></svg><span>+420 555 010 200</span></div>
      <div><svg width="18" height="14" viewBox="0 0 24 18"><rect x="1" y="1" width="22" height="16" fill="#8b7752"/><path d="M1 2l11 8 11-8" fill="none" stroke="#fff" stroke-width="2"/></svg><span>hello@vltavaresidences.com</span></div>
    </div>
  </div>
  <div class="fcol sep" style="width:417px;padding-left:18px">
    <h6>ABOUT US</h6>
    <p class="fabout">Maison Lumen apartments offers short term and as well as long term options in our studio apartments and our one bedroom apartment homes.</p>
  </div>
</footer>

<div class="copy">© VLTAVA RESIDENCES 2017. All Rights Reserved.</div>

</body>
</html>
```